Digital Ad for Savor Parade Valentine's Special Event

Savor Parade is producing a special Valentine's all-inclusive food and beverage +21 tasting event on Saturday February 11, 2023 at the Bluecrest Hangar Gallery in Dallas, TX. We looking for a final push on ticket sales with a digital campaign targeting higher demo meen with this different valentine option then then traditional going out to dinner. And with the Grand Clash on Sunday Feb 12th, maybe there in an angle on making is a Super Weekend or something.

Title – Max length 50 characters
Image type – jpg, jpeg, gif, png
Image size - 300x250, 300x600
Max image size – 100kb
Description Max Length – 160 characters
Call-To-Action button copy max length – 15 characters

```html
<!DOCTYPE html>
<html lang="en">
<head>
<meta charset="utf-8">
<title>Savor Parade Valentine's Special – Display Ads</title>
<link rel="stylesheet" href="https://fonts.googleapis.com/css2?family=Open+Sans:wght@600;700;800&family=Lilita+One&family=Pacifico&display=swap">
<style>
  :root {
    --canvas: #e4e4e4;
    --navy-deep: #141235;
    --navy: #1e1b4d;
    --heart: #1d1a4c;
    --violet: #6a3c8c;
    --violet-soft: #9a5fb0;
    --pink: #d01a55;
    --pink-light: #ff8db3;
    --pink-mid: #ec4f85;
    --ribbon: #3e5aa6;
    --ribbon-dark: #2c4284;
    --white: #ffffff;
    --photo-a: #6b7d5a;
    --photo-b: #8a6a7a;
    --photo-c: #3a3a48;
  }
  * { box-sizing: border-box; margin: 0; padding: 0; }
  html, body { width: 1200px; height: 1071px; overflow: hidden; }
  body { background: var(--canvas); font-family: "Open Sans", sans-serif; position: relative; }

  .ad {
    position: absolute; overflow: hidden; color: var(--white);
    background:
      radial-gradient(ellipse 70% 30% at 50% 30%, rgba(154,95,176,.65), transparent 70%),
      linear-gradient(180deg, var(--navy-deep) 0%, var(--violet) 28%, var(--navy) 55%, var(--navy-deep) 100%);
  }
  .ad--skyscraper { left: 133px; top: 90px; width: 434px; height: 867px; }
  .ad--rectangle { left: 643px; top: 90px; width: 434px; height: 361px;
    background:
      radial-gradient(ellipse 60% 45% at 30% 40%, rgba(154,95,176,.55), transparent 70%),
      linear-gradient(180deg, var(--navy-deep) 0%, var(--violet) 45%, var(--navy) 75%, var(--navy-deep) 100%);
  }

  .brand { position: absolute; text-align: center; }
  .brand__name { font-weight: 800; color: var(--white); line-height: 1; letter-spacing: .5px; }
  .brand__tag { font-weight: 700; text-transform: uppercase; color: var(--white); letter-spacing: .5px; margin-top: 10px; }

  .heart { position: absolute; }
  .heart svg { width: 100%; height: 100%; display: block; }
  .headline { position: absolute; text-align: center; line-height: 1; }
  .headline__super {
    font-family: "Lilita One", sans-serif; display: block;
    color: var(--pink-light);
    background: linear-gradient(180deg, var(--pink-light), var(--pink-mid));
    -webkit-background-clip: text; background-clip: text; -webkit-text-fill-color: transparent;
    transform: skewX(-8deg);
  }
  .headline__weekend { font-family: "Pacifico", cursive; display: block; color: var(--white); }

  .ribbon { position: absolute; }
  .ribbon svg { position: absolute; inset: 0; width: 100%; height: 100%; }
  .ribbon__text { position: relative; text-align: center; font-weight: 700; line-height: 1.2; }

  .photo { position: absolute; background: linear-gradient(120deg, var(--photo-b) 0%, var(--photo-a) 45%, var(--photo-c) 100%); }
  .photo--tall { left: 0; top: 510px; width: 434px; height: 357px; border-radius: 50% 50% 0 0 / 28px 28px 0 0; }
  .photo--wide { left: 211px; top: 139px; width: 223px; height: 185px; }

  .cta {
    position: absolute; display: flex; align-items: center; justify-content: space-between;
    background: var(--pink); border-radius: 4px; font-weight: 700; color: var(--white);
    box-shadow: 0 2px 6px rgba(0,0,0,.35);
  }
  .cta__arrow { background: var(--pink-light); border-radius: 3px; display: flex; align-items: center; justify-content: center; }
  .cta__arrow svg { display: block; }

  .band { position: absolute; left: 0; right: 0; bottom: 0; height: 40px; background: var(--navy-deep); }
</style>
</head>
<body>

<section class="ad ad--skyscraper" aria-label="300 by 600 ad">
  <div class="brand" style="left:0; right:0; top:112px;">
    <div class="brand__name" style="font-size:44px;">Savor Parade</div>
    <div class="brand__tag" style="font-size:14px; margin-top:28px;">Valentine's Special</div>
  </div>

  <div class="heart" style="left:26px; top:229px; width:391px; height:253px;">
    <svg viewBox="0 0 100 90" preserveAspectRatio="none" aria-hidden="true">
      <path d="M50 88 C20 65 0 48 0 26 C0 10 12 0 27 0 C38 0 46 6 50 15 C54 6 62 0 73 0 C88 0 100 10 100 26 C100 48 80 65 50 88Z" fill="var(--heart)"/>
    </svg>
  </div>
  <h1 class="headline" style="left:0; right:0; top:250px;">
    <span class="headline__super" style="font-size:76px;">Super</span>
    <span class="headline__weekend" style="font-size:58px; margin-top:-6px;">Weekend</span>
  </h1>

  <div class="ribbon" style="left:19px; top:403px; width:405px; height:64px;">
    <svg viewBox="0 0 405 64" preserveAspectRatio="none" aria-hidden="true">
      <polygon points="0,14 30,14 30,64 0,64 12,39" fill="var(--ribbon-dark)"/>
      <polygon points="405,14 375,14 375,64 405,64 393,39" fill="var(--ribbon-dark)"/>
      <rect x="20" y="4" width="365" height="52" fill="var(--ribbon)"/>
    </svg>
    <p class="ribbon__text" style="font-size:19px; padding-top:9px;">all-inclusive food and beverage<br>+21 TASTING EVENT</p>
  </div>

  <div class="photo photo--tall" role="img" aria-label="Photo of a couple toasting with glasses of wine at an outdoor table"></div>

  <a class="cta" style="left:48px; top:797px; width:336px; height:48px; padding:0 8px 0 26px; font-size:21px;">
    Get your tickets now!
    <span class="cta__arrow" style="width:34px; height:34px;">
      <svg width="16" height="18" viewBox="0 0 16 18" aria-hidden="true"><polygon points="0,0 16,9 0,18" fill="var(--pink)"/></svg>
    </span>
  </a>
</section>

<section class="ad ad--rectangle" aria-label="300 by 250 ad">
  <div class="photo photo--wide" role="img" aria-label="Photo of a couple toasting with glasses of wine at an outdoor table"></div>
  <div class="band"></div>

  <div class="brand" style="left:10px; width:206px; top:50px;">
    <div class="brand__name" style="font-size:27px;">Savor Parade</div>
    <div class="brand__tag" style="font-size:10px; margin-top:16px;">Valentine's Special</div>
  </div>

  <div class="ribbon" style="left:209px; top:23px; width:205px; height:90px;">
    <svg viewBox="0 0 205 90" preserveAspectRatio="none" aria-hidden="true">
      <polygon points="0,40 20,40 20,90 0,90 8,65" fill="var(--ribbon-dark)"/>
      <polygon points="205,0 185,0 185,50 205,50 197,25" fill="var(--ribbon-dark)"/>
      <rect x="12" y="8" width="180" height="72" fill="var(--ribbon)"/>
    </svg>
    <p class="ribbon__text" style="font-size:15px; padding-top:13px;">all-inclusive food<br>and beverage<br>+21 TASTING EVENT</p>
  </div>

  <div class="heart" style="left:6px; top:125px; width:256px; height:150px;">
    <svg viewBox="0 0 100 90" preserveAspectRatio="none" aria-hidden="true">
      <path d="M50 88 C20 65 0 48 0 26 C0 10 12 0 27 0 C38 0 46 6 50 15 C54 6 62 0 73 0 C88 0 100 10 100 26 C100 48 80 65 50 88Z" fill="var(--heart)"/>
    </svg>
  </div>
  <h2 class="headline" style="left:6px; width:256px; top:140px;">
    <span class="headline__super" style="font-size:46px;">Super</span>
    <span class="headline__weekend" style="font-size:36px; margin-top:-2px;">Weekend</span>
  </h2>

  <a class="cta" style="left:78px; top:299px; width:288px; height:42px; padding:0 6px 0 22px; font-size:18px;">
    Get your tickets now!
    <span class="cta__arrow" style="width:30px; height:30px;">
      <svg width="14" height="16" viewBox="0 0 14 16" aria-hidden="true"><polygon points="0,0 14,8 0,16" fill="var(--pink)"/></svg>
    </span>
  </a>
</section>

</body>
</html>
```